Book cover needed for Christian Non-Fiction Book

I need book cover design (eBook , Paperback, and possibly case laminate Hardcover) for use on PQL and Halvet Print.
Title: Go Forth Called
Sub-Title: Leaving Shelter and Walking in Faithful Purpose
Author: Owen Callery
Also on front cover "Forward by R. Lisel Marrow"

I like clean/simple designs. Below are links to examples of covers I like...
https://www.bookvantle.example/dp/X4821QPT7M?tag=plumwick-20&linkCode=ogi&th=1&psc=1
https://www.bookvantle.example/dp/X49KTRMWHZ?tag=plumwick-20&linkCode=ogi&th=1&psc=1
https://www.bookvantle.example/dp/X22HQC51NT?tag=plumwick-20&linkCode=ogi&th=1&psc=1
https://www.bookvantle.example/dp/X48F3WZPDR?tag=plumwick-20&linkCode=ogi&th=1&psc=1
https://www.bookvantle.example/dp/X4M7UVVCLE?tag=plumwick-20&linkCode=ogi&th=1&psc=1
https://www.bookvantle.example/dp/X2R9HNNKA6?tag=plumwick-20&linkCode=ogi&th=1&psc=1

The main idea for Go Forth Called is that God is a sending God and being "on the move" or journeying is central to God's character, and therefore God's people. I write about our hesitancy to "go," and how the Bible is full of stories about people "going" from Abraham to Jesus, to the disciples of Jesus.

The core biblical text is the Great Commission in Matthew 28:16-20, where Jesus sends out his followers, though some of them doubt.

This paragraph from the forward by R. Lisel Marrow captures the tone of the book well:
This book is a call amid the turmoil. Sacred scripture contains no shortage of narratives in which humans are pulled from their ordinary lives with an inciting incident whose stakes are high. These Biblical figures are lulled from complacency and comfort zones—and yet they are reluctant to serve because they question their ability and influence. Their lessons are relevant for us today: They, and we, are always called and sent with authority. The power of the Holy Spirit equips their “going”—and ours. It’s a sending out that looks less like mastery and more humility. It’s a sending out that is unequivocal service to others modelled in a rabbi-reformer who washed feet and touched the unclean.

I have previously published two shorter books and would be very interested in getting new covers for the old books these so that the three have a similar feel. Whichever designer I go with for "Go Forth Called" I would also want to work with on creating a "branded look" for the other two books.

Target Market(s)

Christian, Religion, Spirituality Readers

Requirements
Must have
• The front cover must have this copy...
Go Forth Called
Leaving Shelter and Walking in Faithful Purpose
Owen Callery
Forward by R. Lisel Marrow

Must be willing to do the full paperback and/or hardcover, but start with thefront cover please
Nice to have
• See attached files for some book covers I like

```html
<!DOCTYPE html>
<html lang="en">
<head>
<meta charset="utf-8">
<title>Go Forth Called — Front Cover</title>
<link rel="stylesheet" href="https://fonts.googleapis.com/css2?family=Cinzel:wght@400&family=Lato:wght@400&display=swap">
<style>
  :root {
    --page-bg: #f4f4f4;
    --cover-black: #050505;
    --photo-mid: #3a3a3a;
    --photo-dark: #161616;
    --ink-white: #ffffff;
    --ink-soft: #e8e8e8;
  }
  * { box-sizing: border-box; margin: 0; padding: 0; }
  html, body {
    width: 1200px; height: 1200px; overflow: hidden;
    background: var(--page-bg);
  }
  .stage {
    width: 1200px; height: 1200px;
    display: flex; align-items: center; justify-content: center;
  }
  .cover {
    position: relative;
    width: 780px; height: 1140px;
    background: var(--cover-black);
    overflow: hidden;
    box-shadow: 0 20px 40px rgba(0,0,0,0.25);
  }
  .cover-photo {
    position: absolute; left: 0; top: 0;
    width: 100%; height: 560px;
    background:
      radial-gradient(ellipse 22% 30% at 50% 26%, #8a8a8a 0%, rgba(90,90,90,0.6) 45%, rgba(0,0,0,0) 100%),
      radial-gradient(ellipse 75% 60% at 50% 55%, var(--photo-mid) 0%, var(--photo-dark) 60%, var(--cover-black) 100%);
  }
  .cover-photo::after {
    content: ""; position: absolute; left: 0; right: 0; bottom: 0; height: 200px;
    background: linear-gradient(to bottom, rgba(5,5,5,0), var(--cover-black));
  }
  .subtitle {
    position: absolute; top: 560px; left: 0; right: 0;
    text-align: center;
    font-family: "Lato", sans-serif;
    font-size: 27px; line-height: 34px;
    color: var(--ink-white);
    text-transform: uppercase;
  }
  .title {
    position: absolute; top: 660px; left: 0; right: 0;
    text-align: center;
    font-family: "Cinzel", serif;
    color: var(--ink-white);
    line-height: 1;
  }
  .title-main {
    display: block;
    font-size: 172px;
    letter-spacing: -2px;
  }
  .title-second {
    display: block;
    font-size: 150px;
    margin-top: 8px;
  }
  .title-o { position: relative; display: inline-block; }
  .title-inset {
    position: absolute; left: 50%; top: 52%;
    transform: translate(-50%, -50%);
    font-size: 44px; letter-spacing: 1px;
  }
  .foreword {
    position: absolute; top: 1010px; left: 0; right: 0;
    text-align: center;
    font-family: "Lato", sans-serif;
    font-size: 20px; letter-spacing: 9px;
    color: var(--ink-soft);
    text-transform: uppercase;
  }
  .author {
    position: absolute; top: 1052px; left: 0; right: 0;
    text-align: center;
    font-family: "Lato", sans-serif;
    font-size: 38px; letter-spacing: 22px;
    color: var(--ink-white);
    text-transform: uppercase;
  }
</style>
</head>
<body>
  <main class="stage">
    <section class="cover">
      <div class="cover-photo" role="img" aria-label="Black and white photo of a person in a dark sweater with hands clasped in prayer"></div>
      <p class="subtitle">Leaving<br>Shelter and<br>Walking in Faithful Purpose</p>
      <h1 class="title">
        <span class="title-main">F<span class="title-o">O<span class="title-inset">GO</span></span>RTH</span>
        <span class="title-second">CALLED</span>
      </h1>
      <p class="foreword">Forward by R. Lisel Marrow</p>
      <p class="author">Owen Callery</p>
    </section>
  </main>
</body>
</html>
```